Flyer Design Project

Advertising - The header is the most important thing on this flyer, I would like to see an eyes-popping more in dept look of the clouds along with the sport car of the couple on the road. The symbol of the "Lantern Over Amber Hills" don't want it there. Just replace it with a regular "i".

Industry/Entity Type

Advertising

Requirements
Must have
• head turning... stopping prospects to read the flyer... everything got to be on point from art works to different fonts and style.

```html
<!DOCTYPE html>
<html lang="en">
<head>
<meta charset="utf-8">
<title>Lantern Over Amber Hills – Flyer</title>
<link href="https://fonts.googleapis.com/css2?family=Arimo:wght@400;700&family=Open+Sans:ital,wght@0,400;0,600;0,700;0,800;1,600;1,700;1,800&family=Raleway:wght@400&family=Roboto+Condensed:ital,wght@0,400;0,700;1,700&display=swap" rel="stylesheet">
<style>
  :root{
    --ink:#26292b;
    --amber:#e09a22;
    --amber-deep:#e8804a;
    --rust:#b3601a;
    --sky-blue:#7eb1d4;
    --panel-blue:#bcd5e6;
    --navy:#162a55;
    --navy-text:#1b2f5e;
    --white:#ffffff;
    --maroon:#8a2a1e;
  }
  *{box-sizing:border-box;margin:0;padding:0}
  html,body{width:1020px;height:1200px;overflow:hidden;background:#ffffff}
  .flyer{position:relative;width:1020px;height:1200px;overflow:hidden;background:var(--sky-blue);font-family:"Roboto Condensed",sans-serif}

  /* Header */
  .hero{position:absolute;left:0;top:0;width:1020px;height:505px;
    background:
      radial-gradient(ellipse 260px 180px at 700px 250px, rgba(255,236,170,.95), rgba(255,200,110,.55) 45%, rgba(255,200,110,0) 75%),
      linear-gradient(180deg,#dfeaf1 0%,#e9e4d6 30%,#f1c88a 48%,#d9843a 62%,#7a3a1c 82%,#3a2218 100%);}
  .hero-title{position:absolute;top:30px;left:0;width:100%;text-align:center;
    font-family:"Open Sans",sans-serif;font-weight:800;color:var(--ink);
    font-size:68px;letter-spacing:-1px;line-height:1;white-space:nowrap}
  .hero-title .accent{font-weight:600;color:var(--amber);font-size:37px;letter-spacing:0;vertical-align:14px;margin:0 4px}
  .hero-tagline{position:absolute;top:105px;left:0;width:100%;text-align:center;
    font-family:"Raleway",sans-serif;font-size:28px;color:#1e1e1e}

  /* Left column */
  .pitch{position:absolute;left:28px;top:522px;width:600px;color:var(--white);font-size:17px;line-height:21px}
  .pitch h2{font-family:"Open Sans",sans-serif;font-weight:700;color:var(--rust);font-size:25px;line-height:29px;margin-bottom:14px}
  .pitch p{margin-bottom:12px}
  .pitch .key{font-weight:700;font-style:italic;color:#1a1a1a;margin:0 4px}
  .pitch .strong{font-weight:700;color:var(--navy-text)}
  .pitch .underline{color:var(--navy-text);border-bottom:1.5px solid var(--navy-text);padding-right:12px}
  .how-title{font-weight:700;color:var(--amber);font-size:23px;line-height:26px;margin-top:4px}
  .steps{list-style:none;margin-bottom:10px}
  .steps li{display:flex;line-height:20px}
  .steps b{width:77px;flex:none;color:var(--navy-text)}
  .never{font-weight:700;color:var(--navy-text);font-size:25px;line-height:30px;margin-bottom:8px}
  .checks{list-style:none}
  .checks li{position:relative;padding-left:24px;line-height:22px;margin-bottom:1px}
  .checks svg{position:absolute;left:0;top:5px}
  .checks .hi{color:var(--amber);font-weight:700;margin:0 3px}

  /* Right column */
  .info-panel{position:absolute;left:660px;top:505px;width:330px;height:595px;background:var(--panel-blue)}
  .burst{position:absolute;left:660px;top:440px;width:320px;height:290px}
  .burst-text{position:absolute;left:666px;top:475px;width:296px;text-align:center;
    font-family:"Open Sans",sans-serif;font-style:italic;font-weight:600;color:var(--maroon);font-size:24px;line-height:28px}
  .burst-text strong{display:block;font-weight:800;color:#1e1e1e;margin-top:2px}
  .contact{position:absolute;left:660px;top:742px;width:330px;text-align:center;font-family:"Arimo",sans-serif;color:#2a2a2a;font-size:16px;line-height:23px}
  .contact .gap{margin-top:12px}
  .contact .orange{color:var(--amber);font-weight:700}
  .contact .phone{font-size:19px}
  .contact .small{font-size:11px;line-height:16px}

  /* Footer */
  .footer{position:absolute;left:0;top:1100px;width:1020px;height:100px;background:var(--navy);color:var(--white)}
  .footer p{font-family:"Open Sans",sans-serif;font-style:italic;font-size:21px;line-height:29px;text-align:center;padding-top:14px}
  .footer small{position:absolute;right:24px;bottom:10px;font-family:"Arimo",sans-serif;font-size:10px}
</style>
</head>
<body>
<div class="flyer">

  <div class="hero" role="img" aria-label="Photograph of a couple with raised arms riding in a white convertible along a winding coastal road at sunset, above a sea of clouds"></div>
  <h1 class="hero-title">LANTERN OVER <span class="accent">AMBER</span>HILLS</h1>
  <p class="hero-tagline">The best way to predict your future is to create it.</p>

  <section class="pitch">
    <h2>What’s the #1 Success Factor<br>in Every Home-Based Business?</h2>
    <p>The answer is <span class="key">DUPLICATION!</span> The key to building a highly successful home-based business is having a <span class="key">SYSTEM</span> in place that everyone can easily follow . . .<br><span class="strong">WE HAVE THAT SYSTEM IN PLACE!</span></p>
    <p>It’s a simple 3 steps proven postcard system that you can plug in immediately.<br><span class="underline">The Entire Process Is Automated.</span></p>
    <h3 class="how-title">HERE’S HOW IT WORKS!</h3>
    <ul class="steps">
      <li><b>Step 1...</b><span>Your prospects receive your postcard in the mail.</span></li>
      <li><b>Step 2...</b><span>They listen to the 24-Hour Information Line and</span></li>
      <li><b>Step 3...</b><span>They contact the Call Center to get their questions<br>answer and then close the sales for you.</span></li>
    </ul>
    <h3 class="never">YOU NEVER HAVE TO SPEAK TO ANYONE!</h3>
    <ul class="checks">
      <li><svg width="14" height="11" viewBox="0 0 14 11"><path d="M1 5.5l4 4 8-8" fill="none" stroke="#1b2f5e" stroke-width="2.2"/></svg>50% fast start bonuses <span class="hi">PAID WEEKLY!</span></li>
      <li><svg width="14" height="11" viewBox="0 0 14 11"><path d="M1 5.5l4 4 8-8" fill="none" stroke="#1b2f5e" stroke-width="2.2"/></svg>Receive a 100% Matching Bonus on all your personal sponsor<br>member’s income <span class="hi">PAID WEEKLY!</span></li>
      <li><svg width="14" height="11" viewBox="0 0 14 11"><path d="M1 5.5l4 4 8-8" fill="none" stroke="#1b2f5e" stroke-width="2.2"/></svg>One-of-a-kind <span class="hi">TWO TEAM</span> compensation plan!</li>
      <li><svg width="14" height="11" viewBox="0 0 14 11"><path d="M1 5.5l4 4 8-8" fill="none" stroke="#1b2f5e" stroke-width="2.2"/></svg>Receive the choice of <span class="hi">50 FREE POST CARDS</span> and <span class="hi">50 FREE LEADS</span> or 20 home business surveyed leads with first month product purchase!</li>
      <li><svg width="14" height="11" viewBox="0 0 14 11"><path d="M1 5.5l4 4 8-8" fill="none" stroke="#1b2f5e" stroke-width="2.2"/></svg>Receive <span class="hi">THREE</span> professional websites for your business for <span class="hi">FREE!</span></li>
      <li><svg width="14" height="11" viewBox="0 0 14 11"><path d="M1 5.5l4 4 8-8" fill="none" stroke="#1b2f5e" stroke-width="2.2"/></svg>Global business already shipping to over 45 countries worldwide and expanding.</li>
      <li><svg width="14" height="11" viewBox="0 0 14 11"><path d="M1 5.5l4 4 8-8" fill="none" stroke="#1b2f5e" stroke-width="2.2"/></svg>30-Day - No Questions Asked, 100% Money Back Guarantee!</li>
    </ul>
  </section>

  <aside class="info-panel"></aside>
  <svg class="burst" viewBox="0 0 320 290" aria-hidden="true">
    <circle cx="168" cy="148" r="140" fill="#e8804a"/>
    <circle cx="158" cy="140" r="138" fill="#e09a22"/>
  </svg>
  <p class="burst-text">100’s of people<br>are joining every day<br>and taking advantage<br>of this once-in-a-<br>lifetime opportunity.<strong>DON’T MISS OUT!</strong></p>

  <div class="contact">
    <p>Call Center Hours<br>Monday thru Friday<br>12PM to 9PM EST<br>Saturday: 12PM to 5PM EST</p>
    <p class="orange phone">PHONE: (555) 214-7730</p>
    <p class="gap">You will need the Call Center<br>Pin number when calling!</p>
    <p class="orange">Call Center Pin<br>Number: K4817</p>
    <p class="gap">24-Hour Information Line:</p>
    <p class="orange">(555) 386-1052</p>
    <p class="small">(Listen before contacting the Call Center)</p>
    <p class="gap">Website:</p>
    <p class="orange">www.lanternamberhills.com</p>
  </div>

  <footer class="footer">
    <p>Due to the high volume of callers, if lines are busy, please keep trying to call into the Call Center<br>or you can just go to the website and get enrolled right away to secure a top position.</p>
    <small>© 2016 Amber Hills Print Collective</small>
  </footer>
</div>
</body>
</html>
```